Business card design needed

I need a business card design also to be used on fridge magnets. All the details above to be included on the card. I am a freelance book-keeper providing services to small to medium size business providing services in LEDGO including training, consulting, BAS, IAS, preparation and lodgement, superannuation, workcover. I would like a design that is easy to read a see. Something that relates to the finance industry. A design that can be used for all other marketing products.

Target Market(s)

Small business mainly sole traders - trades people

Industry/Entity Type

Marketing

Contact Information for Business Card

Keelwind Book-keeping Services Mara Finch - LEDGO Consultant BAS REGISTERED AGENT 57302916 PO Box 7318 Hollowbay North VIC 3917 0417928360

Logo Text

Keelwind Book-keeping Services

Logo styles of interest
Emblem Logo
Pictorial/Combination Logo
Abstract Logo
Character Logo

```html
<!DOCTYPE html>
<html lang="en">
<head>
<meta charset="utf-8">
<title>Mara Finch – Keelwind Book-keeping Services</title>
<link rel="stylesheet" href="https://fonts.googleapis.com/css2?family=EB+Garamond:wght@400;500&family=Open+Sans:wght@400&display=swap">
<style>
  :root {
    --bg-top: #3f474e;
    --bg-mid: #7d8489;
    --bg-bottom: #d3d6d7;
    --text: #f4f5f5;
    --rule: rgba(235, 238, 240, 0.85);
    --suit-dark: #1b2228;
    --suit-mid: #343d45;
    --shirt: #c9cdd1;
  }
  * { margin: 0; padding: 0; box-sizing: border-box; }
  html, body { width: 1200px; height: 693px; overflow: hidden; background: #ffffff; }
  .card {
    position: relative;
    width: 1200px;
    height: 693px;
    overflow: hidden;
    background:
      radial-gradient(ellipse 900px 520px at 30% 0%, var(--bg-top) 0%, rgba(63,71,78,0) 100%),
      linear-gradient(180deg, #4c545a 0%, var(--bg-mid) 45%, #b4b9bc 75%, var(--bg-bottom) 100%);
    color: var(--text);
  }
  .portrait {
    position: absolute;
    top: 0;
    right: 0;
    width: 480px;
    height: 693px;
    background:
      linear-gradient(90deg, rgba(0,0,0,0) 70%, rgba(201,205,209,0.35) 88%, rgba(0,0,0,0) 100%),
      linear-gradient(100deg, rgba(52,61,69,0) 0%, var(--suit-mid) 18%, var(--suit-dark) 55%, #12181d 100%);
  }
  .serif { font-family: "EB Garamond", Georgia, serif; }
  .sans { font-family: "Open Sans", Arial, sans-serif; }
  .line { position: absolute; left: 51px; white-space: nowrap; line-height: 1; }
  .name { top: 62px; font-size: 42px; font-variant: small-caps; letter-spacing: 1px; }
  .company { top: 134px; font-size: 32px; }
  .role { left: 60px; top: 206px; font-size: 40px; font-variant: small-caps; }
  .agent { left: 60px; top: 258px; font-size: 48px; }
  .rule { position: absolute; left: 0; height: 2px; background: var(--rule); }
  .rule-long { top: 321px; width: 643px; }
  .rule-short { top: 335px; width: 622px; }
  .contact { font-size: 33px; letter-spacing: 0.3px; }
  .contact-one { top: 367px; }
  .contact-two { top: 412px; }
</style>
</head>
<body>
  <div class="card">
    <div class="portrait" role="img" aria-label="Photograph of a man in a dark pinstripe suit and tie offering a handshake"></div>

    <div class="line serif name">Mara Finch</div>
    <div class="line sans company">Keelwind Book-keeping Services</div>
    <div class="line serif role">LEDGO Consultant</div>
    <div class="line serif agent">BAS REGISTERED AGENT</div>

    <div class="rule rule-long"></div>
    <div class="rule rule-short"></div>

    <div class="line sans contact contact-one">57302916 PO Box 7318 Hollowbay</div>
    <div class="line sans contact contact-two">North VIC 3917 0417928360</div>
  </div>
</body>
</html>
```